Plumbing Business needs a more appealing business card design and logo

card must include phone number and logo, open to new logo ideas, full creative freedom

Industry/Entity Type

Plumbing

Contact Information for Business Card

Darrell Whitcombe
0417305829

Logo Text

call outs from $80

Font styles to use
• unsure

Colors
ec1f27
0255a3
f78f20

```html
<!DOCTYPE html>
<html lang="en">
<head>
<meta charset="utf-8">
<title>Kellaway Plumbing – Business Card</title>
<link href="https://fonts.googleapis.com/css2?family=Montserrat:wght@500;600;800&display=swap" rel="stylesheet">
<style>
  :root {
    --brand-red: #ec1f27;
    --brand-blue: #0255a3;
    --brand-sky: #46a6dc;
    --brand-orange: #f78f20;
    --paper: #ffffff;
    --ink-grey: #5a5a5a;
    --backdrop: #e9ebee;
  }
  * { box-sizing: border-box; margin: 0; padding: 0; }
  html, body {
    width: 1200px; height: 800px; overflow: hidden;
    background: var(--backdrop);
    font-family: "Montserrat", Arial, sans-serif;
  }
  .canvas {
    width: 1200px; height: 800px;
    display: flex; align-items: center; justify-content: center;
    gap: 60px;
  }
  .card {
    width: 525px; height: 300px;
    border-radius: 22px;
    position: relative;
    overflow: hidden;
    box-shadow: 0 18px 40px rgba(0,0,0,.18);
  }

  /* Front */
  .card--front {
    background: linear-gradient(160deg, var(--brand-sky) 0%, var(--brand-blue) 85%);
    display: flex; flex-direction: column; align-items: center; justify-content: center;
    gap: 18px;
  }
  .brand { display: flex; align-items: center; gap: 12px; }
  .brand__dot {
    width: 26px; height: 26px; border-radius: 50%;
    background: var(--brand-orange); flex: none;
  }
  .brand__name {
    font-weight: 800; text-transform: uppercase; line-height: 1.05;
    letter-spacing: .5px;
  }
  .card--front .brand__name { font-size: 30px; color: var(--paper); }
  .tagline {
    display: flex; align-items: center; gap: 10px;
    font-weight: 600; font-size: 13px; letter-spacing: 1.5px;
    text-transform: uppercase; color: var(--brand-orange);
  }
  .tagline::before, .tagline::after {
    content: ""; width: 40px; height: 2px; background: var(--brand-orange);
  }

  /* Back */
  .card--back { background: var(--paper); }
  .back__mark {
    position: absolute; left: 30px; top: 0; bottom: 0; width: 180px;
    display: flex; flex-direction: column; align-items: center; justify-content: center;
    gap: 16px;
  }
  .back__mark-circle {
    width: 120px; height: 120px; border-radius: 50%;
    background: var(--brand-orange);
  }
  .back__mark .brand__name { font-size: 24px; color: var(--brand-orange); }

  .back__details {
    position: absolute; right: 36px; top: 0; bottom: 0; width: 270px;
    display: flex; flex-direction: column; justify-content: center;
  }
  .back__details .brand__name { font-size: 28px; color: var(--brand-blue); }
  .back__rule {
    height: 2px; background: var(--brand-orange);
    margin: 12px 0 16px; width: 100%;
  }
  .contact__name {
    font-weight: 600; font-size: 16px; letter-spacing: .5px;
    color: var(--brand-blue); text-transform: uppercase;
  }
  .contact__phone {
    margin-top: 8px;
    display: flex; align-items: center; gap: 8px;
    font-weight: 500; font-size: 15px; color: var(--ink-grey);
  }
  .contact__phone svg { width: 15px; height: 15px; flex: none; }
</style>
</head>
<body>
  <main class="canvas">
    <section class="card card--front" aria-label="Card front">
      <div class="brand">
        <span class="brand__dot"></span>
        <span class="brand__name">Kellaway Plumbing</span>
      </div>
      <p class="tagline">Call outs from $80</p>
    </section>

    <section class="card card--back" aria-label="Card back">
      <div class="back__mark">
        <span class="back__mark-circle"></span>
        <span class="brand__name">Kellaway</span>
      </div>
      <div class="back__details">
        <span class="brand__name">Kellaway<br>Plumbing</span>
        <div class="back__rule"></div>
        <p class="contact__name">Darrell Whitcombe</p>
        <p class="contact__phone">
          <svg viewBox="0 0 24 24" aria-hidden="true">
            <path fill="var(--brand-orange)" d="M6.6 10.8a15.1 15.1 0 0 0 6.6 6.6l2.2-2.2a1 1 0 0 1 1-.25 11.4 11.4 0 0 0 3.6.57 1 1 0 0 1 1 1V20a1 1 0 0 1-1 1A17 17 0 0 1 3 4a1 1 0 0 1 1-1h3.5a1 1 0 0 1 1 1c0 1.25.2 2.45.57 3.6a1 1 0 0 1-.25 1z"/>
          </svg>
          0417305829
        </p>
      </div>
    </section>
  </main>
</body>
</html>
```